Health care technology software systems

We have a solid logo. We have company colors that will need to be used as well. We just need a great business card design. We sell to health plans but want to be modern
Updates

Need extra days to review

Target Market(s)

Health technology sector selling into Health Plans

Industry/Entity Type

Health Care Technology

Contact Information for Business Card

Name, title, address, phone number, email

Requirements
Must have
• Use of Kembrata corporate colors - Uploaded w/ our logos

```html
<!DOCTYPE html>
<html lang="en">
<head>
<meta charset="utf-8">
<title>Kembrata Business Card</title>
<link rel="stylesheet" href="https://fonts.googleapis.com/css2?family=Montserrat:wght@300;400;500;600&display=swap">
<style>
  :root {
    --page-bg: #d9d4cd;
    --card-frost: #ebe7e1;
    --card-edge: #f7f5f1;
    --panel-dark: #262626;
    --panel-mid: #3a3a3a;
    --brand-teal: #1c8ea3;
    --brand-green: #7aa83a;
    --text-light: #d6d2cb;
    --text-muted: #bdb7ad;
    --rule: #8a8478;
  }
  html, body {
    margin: 0;
    padding: 0;
    width: 1200px;
    height: 1200px;
    overflow: hidden;
    background: var(--page-bg);
    font-family: "Montserrat", sans-serif;
  }
  .card {
    position: absolute;
    left: 75px;
    top: 315px;
    width: 1050px;
    height: 570px;
    border-radius: 24px;
    overflow: hidden;
    background: var(--card-frost);
    box-shadow: inset 0 0 0 2px var(--card-edge), 0 12px 30px rgba(0,0,0,0.12);
  }
  .card__panel {
    position: absolute;
    inset: 0;
  }
  .card__contact {
    position: absolute;
    left: 0;
    top: 0;
    width: 476px;
    text-align: center;
    color: var(--text-light);
  }
  .contact__name {
    position: absolute;
    left: 0; right: 0;
    top: 68px;
    margin: 0;
    font-size: 35px;
    font-weight: 500;
    letter-spacing: 1.5px;
    color: var(--brand-teal);
  }
  .contact__title {
    position: absolute;
    left: 0; right: 0;
    top: 116px;
    margin: 0;
    font-size: 25px;
    font-weight: 300;
    color: var(--text-light);
  }
  .contact__icons {
    position: absolute;
    left: 60px;
    top: 193px;
    width: 356px;
  }
  .contact__lines {
    position: absolute;
    left: 0; right: 0;
    top: 255px;
    margin: 0;
    font-size: 25px;
    font-weight: 300;
    line-height: 37px;
  }
  .contact__web strong {
    font-weight: 500;
    color: var(--brand-green);
  }
  .contact__rule {
    position: absolute;
    left: 85px;
    width: 306px;
    top: 398px;
    height: 1px;
    background: var(--rule);
  }
  .contact__address {
    position: absolute;
    left: 0; right: 0;
    top: 430px;
    margin: 0;
    font-size: 25px;
    font-weight: 300;
    line-height: 37px;
    font-style: normal;
    color: var(--text-muted);
  }
  .card__brand {
    position: absolute;
    left: 480px;
    top: 0;
    width: 552px;
    height: 570px;
    display: flex;
    align-items: center;
    justify-content: center;
    font-size: 62px;
    font-weight: 500;
    color: var(--brand-teal);
    letter-spacing: 1px;
  }
</style>
</head>
<body>
  <div class="card">
    <svg class="card__panel" width="1050" height="570" viewBox="0 0 1050 570" aria-hidden="true">
      <defs>
        <linearGradient id="panelShade" x1="0" y1="0" x2="1" y2="0">
          <stop offset="0" stop-color="#2b2b2b"/>
          <stop offset="0.55" stop-color="#333333"/>
          <stop offset="1" stop-color="#1e1e1e"/>
        </linearGradient>
        <mask id="panelCut">
          <rect width="1050" height="570" fill="#fff"/>
          <circle cx="756" cy="286" r="318" fill="#000"/>
        </mask>
      </defs>
      <rect width="760" height="570" fill="url(#panelShade)" mask="url(#panelCut)"/>
    </svg>

    <div class="card__contact">
      <h1 class="contact__name">NEIL ARDMORE</h1>
      <p class="contact__title">President</p>

      <svg class="contact__icons" width="356" height="34" viewBox="0 0 356 34" aria-hidden="true">
        <line x1="0" y1="17" x2="115" y2="17" stroke="var(--rule)" stroke-width="1"/>
        <line x1="241" y1="17" x2="356" y2="17" stroke="var(--rule)" stroke-width="1"/>
        <g fill="var(--brand-green)">
          <circle cx="134" cy="17" r="14"/>
          <circle cx="178" cy="17" r="14"/>
          <circle cx="222" cy="17" r="14"/>
        </g>
        <g fill="none" stroke="#2c2c2c" stroke-width="2" stroke-linecap="round">
          <path d="M128 10 q-2 7 4 13 q6 5 10 3 l-1 -4 -4 -1 -2 2 q-4 -2 -6 -6 l2 -2 -1 -4 z" fill="#2c2c2c" stroke="none"/>
          <rect x="173" y="8" width="10" height="18" rx="2"/>
          <line x1="176" y1="23" x2="180" y2="23"/>
          <circle cx="222" cy="17" r="8"/>
          <ellipse cx="222" cy="17" rx="3.5" ry="8"/>
          <line x1="214" y1="17" x2="230" y2="17"/>
        </g>
      </svg>

      <p class="contact__lines">
        <span class="contact__phone">949-555-0183</span><br>
        <span class="contact__email">nardmore@kembrata.com</span><br>
        <span class="contact__web">www.<strong>kembrata</strong>.com</span>
      </p>

      <div class="contact__rule"></div>

      <address class="contact__address">
        18420 Harbor Crest<br>
        Laguna Vista CA 92651
      </address>
    </div>

    <div class="card__brand">Kembrata</div>
  </div>
</body>
</html>
```